Quillmont Booking Engine Marketing Site

Hi,
I’m currently in the process of putting together a web application with the intention of providing small resorts/B&Bs/small hotels the ability to allow their customers to book online.
I’m looking to have a design created for a marketing site, to give potential customers additional information about my booking engine, as well as to help drive sign-ups. A lot of the competition out there appears outdated, so I would like something that is more modern and up to date.
I am looking for just the design (i’m a web developer, but I lack the creative skills for a good marketing site)
For some more background, I will be targeting business owners of smaller resorts and Bed & Breakfasts. These are typically family owned small businesses that may only have a 10 room setup. These businesses will also typically have additional amenities that they will have to rent out or sell to their clients ( ex. Spa, fruit basket, water sport rentals). My software will provide them with the ability to sell their amenities as well.
I’m open to different designs, but my main thing is I want it to look modern, and I want it to have several callouts to sign up for my product.
I am looking to have the homepage created, 1 interior page, and a style guide created (to show form fields, H1’s, etc.).
I had a logo created a couple months ago that will be included with this project brief.
If you need any additional information feel free to reach out to me.

Target Market(s)

This site will be targeted small business owners who are running small resorts, Bed and Breakfasts, or any business that provides rooms for their clients.

Industry/Entity Type

Saas

Number of Pages Required

2 page

Font styles to use
Sans Serif

Colors

Designer to choose colors to be used in the design.

Requirements
Must have
• A modern feel, with several CTA's that will drive to the registration page on the homepage. on the internal page, I mostly just need the page layout, I will reuse that page layout. and a style guide if at all possible (include colors, form fields, H1's, etc.)
Nice to have
• maybe a hero image at the top with buttons over the top? again i'm pretty open to most anything.
Should not have
• I like images, but I don't want the page overrun with images. A good balance.

```html
<!DOCTYPE html>
<html lang="en">
<head>
<meta charset="utf-8">
<title>Quillmont Booking Engine – Style Guide</title>
<link href="https://fonts.googleapis.com/css2?family=Montserrat:wght@300;400;500;600;700&display=swap" rel="stylesheet">
<style>
:root{
  --ink:#2b2b2b;
  --ink-soft:#5a5a5a;
  --muted:#9aa0a6;
  --line:#e1e4e8;
  --paper:#f5f6f8;
  --white:#ffffff;
  --teal:#40c1ca;
  --orange:#fe5b2c;
  --navy:#00558d;
  --blue:#1a7fe6;
  --blue-light:#4fa3f7;
  --green:#7ab51d;
  --red:#e2463d;
  --error-bg:#fdecea;
}
*{box-sizing:border-box;margin:0;padding:0}
html,body{width:1200px;height:3272px;overflow:hidden}
body{font-family:"Montserrat",Arial,sans-serif;color:var(--ink);background:var(--paper)}
.page{position:relative;width:1200px;height:3272px;overflow:hidden;background:var(--paper)}
.abs{position:absolute}

/* header */
.brand{position:absolute;left:48px;top:28px;display:flex;align-items:center;gap:14px}
.brand-dot{width:40px;height:40px;border-radius:50%;background:var(--green)}
.brand-name{font-weight:700;font-size:22px;line-height:1.05;color:var(--navy);width:170px}
.doc-title{position:absolute;left:340px;top:46px;font-size:20px;font-weight:500;color:var(--ink-soft)}
.rule{position:absolute;left:48px;width:1104px;height:1px;background:var(--line)}

.section-title{position:absolute;font-size:22px;font-weight:400;color:var(--ink-soft);letter-spacing:1px;text-transform:uppercase}
.section-title span{font-size:11px;color:var(--muted);margin-right:14px;vertical-align:middle}

/* palette */
.swatches{position:absolute;left:48px;top:216px;display:flex;gap:22px}
.swatch{width:116px}
.swatch-chip{height:100px;border-radius:4px}
.swatch-code{margin-top:16px;font-size:12px;color:var(--ink-soft);text-align:center}

/* typography */
.type-hero{position:absolute;left:48px;top:470px;font-size:110px;font-weight:300;color:var(--muted)}
.type-row{position:absolute;left:48px;display:flex;color:var(--muted)}
.type-row .name{width:260px}
.type-row .spec{font-weight:300}
.lh-label{position:absolute;left:660px;top:600px;font-size:11px;color:var(--ink-soft)}
.lh-mark{position:absolute;left:612px;font-size:10px;color:var(--red)}
.lh-bar{position:absolute;left:650px;width:2px;background:var(--red)}
.sample-h1{position:absolute;left:660px;top:690px;font-size:46px;font-weight:600;color:var(--blue)}
.sample-h2{position:absolute;left:660px;top:752px;font-size:30px;font-weight:500;color:var(--navy)}
.sample-p{position:absolute;left:660px;top:818px;width:470px;font-size:17px;line-height:1.55;color:var(--ink-soft)}

/* buttons */
.small-label{position:absolute;font-size:12px;color:var(--muted)}
.btn{position:absolute;height:52px;border-radius:26px;font-size:15px;font-weight:700;display:flex;align-items:center;justify-content:center}
.btn-primary{background:var(--blue);color:var(--white)}
.btn-primary.is-hover{background:var(--blue);box-shadow:0 10px 18px rgba(26,127,230,.35)}
.btn-secondary{background:var(--white);color:var(--blue);box-shadow:0 3px 8px rgba(0,0,0,.08)}
.btn-secondary.is-hover{box-shadow:0 10px 20px rgba(0,0,0,.14)}
.link{position:absolute;font-size:14px;color:var(--blue)}
.link.is-hover{text-decoration:underline}
.link.is-disabled{color:var(--muted)}
.btn-small{position:absolute;height:40px;width:140px;border-radius:20px;background:var(--green);color:var(--white);font-size:13px;font-weight:600;display:flex;align-items:center;justify-content:center}
.btn-small.is-hover{box-shadow:0 8px 16px rgba(122,181,29,.45)}
.btn-small.is-active{background:#6aa10f}

/* navigation */
.nav{position:absolute;left:680px;display:flex;gap:36px;font-size:16px;font-weight:600;color:var(--ink)}
.nav .current{color:var(--blue);border-bottom:3px solid var(--blue);padding-bottom:6px}
.nav-box{position:absolute;left:680px;width:470px;height:56px;background:var(--white);border:1px solid var(--line);display:flex;font-size:16px;font-weight:600}
.nav-box div{flex:1;display:flex;align-items:center;justify-content:center;border-right:1px solid var(--line)}
.nav-box div:last-child{border-right:0}
.nav-box .current{background:var(--blue);color:var(--white)}

/* icons */
.icons{position:absolute;left:48px;display:flex;gap:84px}
.icons svg{width:64px;height:64px}

/* forms */
.field{position:absolute;left:80px;width:300px;height:44px;background:var(--white);border:1px solid #cfd4da;border-radius:3px;padding:0 14px;display:flex;align-items:center;font-size:14px;color:var(--ink-soft)}
.field.is-active{border-color:var(--orange)}
.field.is-error{border-color:var(--red);background:var(--error-bg);color:var(--red)}
.field-help{position:absolute;left:80px;font-size:11px;color:var(--red)}
.textarea{position:absolute;left:80px;top:2248px;width:300px;height:84px;background:var(--white);border:1px solid #cfd4da;border-radius:3px;padding:12px 14px;font-size:13px;color:var(--muted)}
.check{position:absolute;width:22px;height:22px;border:2px solid #c3c8ce;background:var(--white)}
.check.round{border-radius:50%}
.select{position:absolute;left:820px;width:340px;height:48px;background:var(--white);border:1px solid #cfd4da;border-radius:3px;padding:0 16px;display:flex;align-items:center;justify-content:space-between;font-size:15px;color:var(--ink)}
.select-list{position:absolute;left:820px;top:2156px;width:340px;background:var(--white);border:1px solid #cfd4da;font-size:15px}
.select-list div{height:44px;padding:0 16px;display:flex;align-items:center}
.select-list .hover{background:var(--blue);color:var(--white)}

/* cards */
.card{position:absolute;top:2360px;height:500px;background:var(--white);border-radius:4px;box-shadow:0 4px 14px rgba(0,0,0,.08)}
.cal-head{position:absolute;left:0;top:24px;width:100%;display:flex;justify-content:space-between;padding:0 28px;font-size:16px;font-weight:600}
.cal-grid{position:absolute;left:24px;top:80px;display:grid;grid-template-columns:repeat(7,44px);row-gap:14px;font-size:13px;text-align:center;color:var(--ink-soft)}
.cal-grid .wd{color:var(--muted);font-size:11px}
.cal-grid .sel{background:var(--green);color:var(--white);border-radius:50%;width:32px;height:32px;line-height:32px;margin:-8px auto 0}
.filter-row{position:absolute;left:24px;right:24px;font-size:12px;color:var(--ink-soft);display:flex;justify-content:space-between}
.filter-line{position:absolute;left:24px;right:24px;height:1px;background:var(--line)}
.mini-input{position:absolute;width:70px;height:30px;border:1px solid #cfd4da;border-radius:3px;font-size:11px;color:var(--ink-soft);display:flex;align-items:center;padding-left:8px}
.cat-row{position:absolute;left:24px;right:24px;height:38px;border-bottom:1px solid var(--line);font-size:13px;color:var(--ink);display:flex;align-items:center;justify-content:space-between}
.cat-sub{position:absolute;left:44px;font-size:12px;color:var(--blue-light)}

/* footer logos */
.logo-panel{position:absolute;top:2940px;width:400px;height:332px;display:flex;align-items:center;justify-content:center;gap:14px}
.logo-panel .brand-name{width:180px}
</style>
</head>
<body>
<div class="page">

  <header>
    <div class="brand"><div class="brand-dot"></div><div class="brand-name">Quillmont<br>Booking Engine</div></div>
    <div class="doc-title">Style Guide</div>
  </header>
  <div class="rule" style="top:118px"></div>

  <!-- 01 colour palette -->
  <h2 class="section-title" style="left:48px;top:150px"><span>01</span>Colour Palette</h2>
  <div class="swatches">
    <div class="swatch"><div class="swatch-chip" style="background:var(--ink)"></div><div class="swatch-code">#2B2B2B</div></div>
    <div class="swatch"><div class="swatch-chip" style="background:var(--ink-soft)"></div><div class="swatch-code">#5A5A5A</div></div>
    <div class="swatch"><div class="swatch-chip" style="background:#f3f3f3;border:1px solid var(--line)"></div><div class="swatch-code">#F3F3F3</div></div>
    <div class="swatch"><div class="swatch-chip" style="background:var(--teal)"></div><div class="swatch-code">#40C1CA</div></div>
    <div class="swatch"><div class="swatch-chip" style="background:var(--orange)"></div><div class="swatch-code">#FE5B2C</div></div>
    <div class="swatch"><div class="swatch-chip" style="background:var(--navy)"></div><div class="swatch-code">#00558D</div></div>
    <div class="swatch"><div class="swatch-chip" style="background:var(--blue-light)"></div><div class="swatch-code">#4FA3F7<br>#1A7FE6</div></div>
    <div class="swatch"><div class="swatch-chip" style="background:var(--green)"></div><div class="swatch-code">#7AB51D</div></div>
  </div>
  <div class="rule" style="top:400px"></div>

  <!-- 02 typography -->
  <h2 class="section-title" style="left:48px;top:432px"><span>02</span>Typography</h2>
  <div class="type-hero">Montserrat</div>
  <div class="type-row" style="top:640px;font-size:40px"><div class="name">Title</div><div class="spec">Light 40px</div></div>
  <div class="type-row" style="top:712px;font-size:30px"><div class="name">Subheader</div><div class="spec" style="font-weight:400">Regular 30px</div></div>
  <div class="type-row" style="top:770px;font-size:18px;font-weight:700"><div class="name">Menu/Button</div><div class="spec" style="font-weight:700">Bold 18px</div></div>
  <div class="type-row" style="top:814px;font-size:18px"><div class="name">Body 1</div><div class="spec" style="font-weight:400">Regular 18px</div></div>
  <div class="type-row" style="top:856px;font-size:16px"><div class="name">Paragraph</div><div class="spec" style="font-weight:400">Regular 16px</div></div>

  <div class="lh-label">LINE HEIGHT</div>
  <div class="lh-bar" style="top:708px;height:46px"></div>
  <div class="lh-mark" style="top:722px">31 px</div>
  <div class="lh-bar" style="top:768px;height:30px"></div>
  <div class="lh-mark" style="top:776px">40 px</div>
  <div class="sample-h1">Quillmont Booking</div>
  <div class="sample-h2">Manage Hotel or BnB</div>
  <p class="sample-p">Quillmont Booking Engine is a online booking service. It's a centralized platform where service providers can manage various aspects of their business with absolute ease.</p>
  <div class="rule" style="top:1032px"></div>

  <!-- 03 buttons -->
  <h2 class="section-title" style="left:48px;top:1064px"><span>03</span>Buttons</h2>
  <div class="small-label" style="left:80px;top:1118px">FILLED BUTTONS</div>
  <div class="small-label" style="left:80px;top:1152px">Normal</div>
  <div class="btn btn-primary" style="left:80px;top:1176px;width:240px">Join Quillmont</div>
  <div class="small-label" style="left:360px;top:1152px">Normal</div>
  <div class="btn btn-secondary" style="left:360px;top:1176px;width:240px">Join Quillmont</div>
  <div class="small-label" style="left:80px;top:1256px">Hover</div>
  <div class="btn btn-primary is-hover" style="left:80px;top:1280px;width:240px">Join Quillmont</div>
  <div class="small-label" style="left:360px;top:1256px">Hover</div>
  <div class="btn btn-secondary is-hover" style="left:360px;top:1280px;width:240px">Join Quillmont</div>
  <div class="link" style="left:80px;top:1462px">Link 1</div>
  <div class="link is-hover" style="left:230px;top:1462px">Link (Tapped/Hover)</div>
  <div class="link is-disabled" style="left:460px;top:1462px">Link (Disabled)</div>
  <div class="btn-small" style="left:80px;top:1500px">Button</div>
  <div class="btn-small is-hover" style="left:250px;top:1500px">Hover</div>
  <div class="btn-small is-active" style="left:420px;top:1500px">Active</div>

  <!-- 04 navigation -->
  <h2 class="section-title" style="left:620px;top:1064px"><span>04</span>Navigation</h2>
  <div class="small-label" style="left:680px;top:1118px">Primary Menu (Normal)</div>
  <nav class="nav" style="top:1146px"><div>About</div><div>How It Works</div><div>Plans</div></nav>
  <div class="small-label" style="left:680px;top:1196px">Primary Menu (Hover / Active)</div>
  <nav class="nav" style="top:1224px"><div class="current">About</div><div>How It Works</div><div>Plans</div></nav>
  <div class="small-label" style="left:680px;top:1290px">Secondary Menu (Normal)</div>
  <nav class="nav-box" style="top:1314px"><div>About</div><div>How It Works</div><div>Plans</div></nav>
  <div class="small-label" style="left:680px;top:1410px">Secondary Menu (Hover / Active)</div>
  <nav class="nav-box" style="top:1434px"><div class="current">About</div><div>How It Works</div><div>Plans</div></nav>
  <div class="rule" style="top:1580px"></div>

  <!-- 05 icons -->
  <h2 class="section-title" style="left:48px;top:1612px"><span>05</span>Icons</h2>
  <div class="icons" style="top:1690px">
    <svg viewBox="0 0 64 64"><circle cx="32" cy="32" r="26" fill="none" stroke="var(--green)" stroke-width="4"/><path d="M20 33l9 9 16-18" fill="none" stroke="var(--green)" stroke-width="5" stroke-linecap="round" stroke-linejoin="round"/></svg>
    <svg viewBox="0 0 64 64"><path d="M14 28h30v12a12 12 0 0 1-12 12h-6a12 12 0 0 1-12-12z" fill="none" stroke="var(--ink-soft)" stroke-width="3"/><path d="M44 32h4a5 5 0 0 1 0 10h-5" fill="none" stroke="var(--ink-soft)" stroke-width="3"/><path d="M22 12v10M30 10v12M38 12v10" stroke="var(--orange)" stroke-width="3" stroke-linecap="round"/></svg>
    <svg viewBox="0 0 64 64"><rect x="8" y="12" width="48" height="32" rx="2" fill="none" stroke="var(--ink-soft)" stroke-width="3"/><rect x="13" y="17" width="38" height="22" fill="var(--teal)"/><path d="M24 54h16M32 44v10" stroke="var(--ink-soft)" stroke-width="3"/></svg>
    <svg viewBox="0 0 64 64"><rect x="14" y="8" width="36" height="48" rx="2" fill="none" stroke="var(--ink-soft)" stroke-width="3"/><path d="M21 20h22M21 28h22M21 36h22M21 44h14" stroke="var(--blue)" stroke-width="3"/></svg>
    <svg viewBox="0 0 64 64"><path d="M14 8h26l10 10v38H14z" fill="none" stroke="var(--ink-soft)" stroke-width="3"/><path d="M21 26h22M21 34h22M21 42h16" stroke="var(--teal)" stroke-width="3"/></svg>
    <svg viewBox="0 0 64 64"><rect x="10" y="12" width="40" height="16" rx="8" fill="var(--orange)"/><circle cx="42" cy="20" r="6" fill="#fff"/><rect x="14" y="36" width="40" height="16" rx="8" fill="var(--teal)"/><circle cx="22" cy="44" r="6" fill="#fff"/></svg>
    <svg viewBox="0 0 64 64"><path d="M8 32L32 10l24 22" fill="none" stroke="var(--ink-soft)" stroke-width="3"/><path d="M16 28v26h32V28" fill="none" stroke="var(--ink-soft)" stroke-width="3"/><rect x="27" y="38" width="10" height="16" fill="var(--blue)"/></svg>
  </div>
  <div class="icons" style="top:1816px">
    <svg viewBox="0 0 64 64"><path d="M22 12h20l6 18H16z" fill="var(--ink-soft)"/><path d="M32 30v18M22 52h20" stroke="var(--ink-soft)" stroke-width="3"/></svg>
    <svg viewBox="0 0 64 64"><path d="M8 18v34M56 36v16M8 44h48M8 36h48" stroke="var(--ink-soft)" stroke-width="3"/><rect x="12" y="26" width="12" height="8" rx="3" fill="var(--ink-soft)"/></svg>
    <svg viewBox="0 0 64 64"><path d="M8 24l6-12h36l6 12z" fill="var(--ink-soft)"/><rect x="12" y="24" width="40" height="28" fill="none" stroke="var(--ink-soft)" stroke-width="3"/><rect x="26" y="36" width="12" height="16" fill="var(--ink-soft)"/></svg>
    <svg viewBox="0 0 64 64"><circle cx="32" cy="32" r="24" fill="var(--blue-light)"/><path d="M22 28l10 10 10-10" fill="none" stroke="#fff" stroke-width="4" stroke-linecap="round"/></svg>
    <svg viewBox="0 0 64 64"><circle cx="32" cy="32" r="9" fill="#b8bec5"/></svg>
    <svg viewBox="0 0 64 64"><circle cx="32" cy="32" r="9" fill="#b8bec5"/></svg>
    <svg viewBox="0 0 64 64"><circle cx="32" cy="32" r="9" fill="#b8bec5"/></svg>
  </div>
  <div class="rule" style="top:1926px"></div>

  <!-- 06 forms -->
  <h2 class="section-title" style="left:48px;top:1956px"><span>06</span>Forms</h2>
  <div class="small-label" style="left:80px;top:2006px">Text Input</div>
  <div class="field" style="top:2036px">Text</div>
  <div class="field is-active" style="top:2110px">Active Input field</div>
  <div class="field is-error" style="top:2180px">Error</div>
  <div class="field-help" style="top:2230px">Something is wrong with this field</div>
  <div class="textarea">Text Area</div>

  <div class="small-label" style="left:500px;top:2006px">Checkbox / Radio</div>
  <div class="check" style="left:512px;top:2040px"></div>
  <div class="check" style="left:512px;top:2082px;border-color:var(--green)"></div>
  <div class="check round" style="left:512px;top:2124px"></div>
  <div class="check round" style="left:572px;top:2124px"></div>
  <div class="check round" style="left:512px;top:2168px;border-color:var(--green);background:radial-gradient(circle,var(--green) 0 5px,#fff 6px)"></div>
  <div class="check" style="left:572px;top:2168px;border-color:var(--green);background:var(--green)"></div>

  <div class="select" style="top:2034px">Choose something <span>▾</span></div>
  <div class="select" style="top:2108px;border-color:var(--blue)">Choose something <span>▾</span></div>
  <div class="select-list"><div>Option 1</div><div class="hover">Option 2</div><div>Option 3</div></div>

  <!-- calendar -->
  <div class="card" style="left:72px;width:360px">
    <div class="cal-head"><span>‹</span><span>7 January 2017</span><span>›</span></div>
    <div class="cal-grid">
      <div class="wd">S</div><div class="wd">M</div><div class="wd">T</div><div class="wd">W</div><div class="wd">T</div><div class="wd">F</div><div class="wd">S</div>
      <div>1</div><div>2</div><div>3</div><div>4</div><div>5</div><div>6</div><div>7</div>
      <div>8</div><div>9</div><div>10</div><div>11</div><div>12</div><div>13</div><div>14</div>
      <div><div class="sel">15</div></div><div>16</div><div>17</div><div>18</div><div>19</div><div>20</div><div>21</div>
      <div>22</div><div>23</div><div>24</div><div>25</div><div>26</div><div>27</div><div>28</div>
      <div>29</div><div>30</div><div>31</div><div></div><div></div><div></div><div></div>
    </div>
  </div>

  <!-- filter -->
  <div class="card" style="left:460px;width:300px">
    <div class="filter-row" style="top:22px"><strong>Filters</strong><span style="color:var(--muted)">Clear all ✕</span></div>
    <div class="filter-line" style="top:52px"></div>
    <div class="filter-row" style="top:66px"><span>Guest</span></div>
    <div class="mini-input" style="left:24px;top:92px">Rooms ▾</div>
    <div class="mini-input" style="left:110px;top:92px">Nights ▾</div>
    <div class="mini-input" style="left:196px;top:92px">Adults ▾</div>
    <div class="mini-input" style="left:24px;top:134px">Kids ▾</div>
    <div class="mini-input" style="left:110px;top:134px">Pets ▾</div>
    <div class="mini-input" style="left:196px;top:134px">Parking</div>
    <div class="filter-line" style="top:186px"></div>
    <div class="filter-row" style="top:200px"><span>Price range</span></div>
    <div class="mini-input" style="left:24px;top:226px;width:250px">Any price</div>
    <div class="abs" style="left:24px;top:280px;width:250px;height:4px;background:var(--line)"></div>
    <div class="abs" style="left:60px;top:280px;width:150px;height:4px;background:var(--blue)"></div>
    <div class="abs" style="left:52px;top:274px;width:16px;height:16px;border-radius:50%;background:var(--blue)"></div>
    <div class="abs" style="left:202px;top:274px;width:16px;height:16px;border-radius:50%;background:var(--blue)"></div>
    <div class="mini-input" style="left:36px;top:304px">$10</div>
    <div class="mini-input" style="left:170px;top:304px">$500</div>
    <div class="filter-line" style="top:356px"></div>
    <div class="filter-row" style="top:370px"><span>Another option</span><span>›</span></div>
    <div class="filter-line" style="top:400px"></div>
    <div class="filter-row" style="top:414px"><span>Pricing option</span><span>›</span></div>
    <div class="btn-small" style="left:80px;top:446px">Apply filters</div>
  </div>

  <!-- categories -->
  <div class="card" style="left:840px;width:320px">
    <div class="cat-row" style="top:14px;font-weight:600">Categories</div>
    <div class="cat-row" style="top:52px">Computers<span>›</span></div>
    <div class="cat-row" style="top:90px">Monitors<span>›</span></div>
    <div class="cat-row" style="top:128px;border:0">Projectors<span>⌄</span></div>
    <div class="cat-sub" style="top:174px">Internal</div>
    <div class="cat-sub" style="top:202px">External</div>
    <div class="cat-sub" style="top:230px">Led</div>
    <div class="cat-sub" style="top:258px">Small</div>
    <div class="cat-row" style="top:290px;border-top:1px solid var(--line)">Lights<span>›</span></div>
    <div class="cat-row" style="top:328px">Controllers<span>›</span></div>
    <div class="cat-row" style="top:366px">Console<span>›</span></div>
    <div class="cat-row" style="top:404px">Extras<span>›</span></div>
  </div>

  <!-- logo variants -->
  <div class="logo-panel" style="left:0;background:var(--white)"><div class="brand-dot"></div><div class="brand-name">Quillmont<br>Booking Engine</div></div>
  <div class="logo-panel" style="left:400px;background:var(--blue)"><div class="brand-dot" style="background:var(--white)"></div><div class="brand-name" style="color:var(--white)">Quillmont<br>Booking Engine</div></div>
  <div class="logo-panel" style="left:800px;background:#eceef1"><div class="brand-dot" style="background:var(--ink-soft)"></div><div class="brand-name" style="color:var(--ink-soft)">Quillmont<br>Booking Engine</div></div>

</div>
</body>
</html>
```